Design Fresh and modern brochure about hypnosis

We need a clean and modern brochure designed for our hypnosis center. I have text, a logo, and a single image. I'd like all placed in a tri-fold brochure with design elements added and I'd like the result in a format which can be modified, like InDesign. The brochure should appear modern and clean, but also with a softer look to appear compassionate. The company values are professional, compassionate, and local. Local is the Pacific Northwest. Colors should match the logo, blue with elements of water. I'd like to see shades of blue with white.
Updates

Hello designers. Thank you all for your great brochure designs thus far. 

At this time I've narrowed down the top 2 designs and those designers have been contacted. 

So right now, any new designs would be in consideration for third place. I want to be fair to your time, so please consider if you're still interested in submitting a design for 3rd place or not. 

Thank you. 

Target Market(s)

Adults in western US who want to improve their lives. Primarily 30+ in age, english speaking, and working full or part time.

Industry/Entity Type

It Company

Colors
85cae6
0555a3
3276b5
86cfc6
32b7a4

Requirements
Must have
• The brochure must include the logo and image attached, and should fit in the tri-fold design, similar to the example brochure. It also needs to be in a format that can be easily modified over time, as I typically change text in the brochure. InDesign would be great.
Nice to have
• Additional design elements - like areas for a call-out to highlight features.

```html
<!DOCTYPE html>
<html lang="en">
<head>
<meta charset="utf-8">
<title>Tidewater Hypnosis Center – Tri-fold Brochure</title>
<link rel="stylesheet" href="https://fonts.googleapis.com/css2?family=Open+Sans:wght@400;600;700&display=swap">
<style>
  :root{
    --slate:#3b5861;
    --sky:#6cc5dc;
    --ocean:#4aa3b8;
    --seafoam:#8fd0c6;
    --mist:#ededed;
    --mist-dark:#e6e6e6;
    --ink:#555c60;
    --ink-dark:#3d4a50;
    --logo:#5f8fa0;
    --list:#8fd6ea;
    --white:#ffffff;
  }
  *{margin:0;padding:0;box-sizing:border-box;}
  html,body{width:800px;height:1200px;overflow:hidden;background:var(--white);}
  body{position:relative;font-family:"Open Sans",Arial,sans-serif;color:var(--ink);}
  .block{position:absolute;}
  .photo{position:absolute;}
  .waves{position:absolute;left:0;top:0;width:800px;height:1200px;pointer-events:none;}
  .layer{position:absolute;}

  /* panels */
  .panel-slate{background:var(--slate);}
  .panel-mist{background:var(--mist);}
  .panel-mist-dark{background:var(--mist-dark);}

  /* placeholders */
  .ph-stones{background:linear-gradient(180deg,#eaf4f6 0%,#b9d9e0 45%,#6f9fab 100%);}
  .ph-stones-row{background:linear-gradient(180deg,#d7eaef 0%,#a6cdd7 60%,#7fb4c2 100%);}
  .ph-portrait{background:linear-gradient(180deg,#dfe9f1 0%,#a9c3d8 35%,#3f7ca3 55%,#6d6a62 80%,#4b4944 100%);}
  .ph-falls{background:linear-gradient(160deg,#7f9a9f 0%,#b8e1ea 35%,#64c3da 55%,#4f6e74 80%,#8aa7ad 100%);}
  .ph-hill{background:linear-gradient(180deg,#cfe2e8 0%,#a9c6cf 40%,#6d9aa5 70%,#4f7c86 100%);}

  /* logo */
  .brand{position:absolute;text-align:center;color:var(--logo);font-weight:400;}
  .brand-name{display:block;letter-spacing:.2em;text-transform:uppercase;}
  .brand-sub{display:block;letter-spacing:.08em;}

  /* top-left list */
  .services{position:absolute;left:48px;top:270px;width:236px;color:var(--list);text-align:center;}
  .services h3{font-size:8.6px;font-weight:700;margin-bottom:22px;}
  .services-cols{display:flex;justify-content:center;gap:22px;font-size:8.4px;line-height:1.27;}
  .services-cols ul{list-style:none;}
  .services .more{font-size:8.2px;margin-top:16px;}
  .services .contact{font-size:8.2px;font-weight:700;margin-top:74px;line-height:1.35;}

  .contact-block{position:absolute;left:284px;top:266px;width:233px;text-align:center;font-size:9.6px;line-height:1.35;color:var(--ink-dark);}
  .contact-block .web{margin-top:12px;}

  .tagline{position:absolute;left:517px;top:522px;width:235px;text-align:center;font-size:14px;line-height:1.35;color:var(--ink-dark);}

  /* inside copy */
  .copy{position:absolute;font-size:6.6px;line-height:1.28;}
  .copy h2{font-size:10px;font-weight:700;text-align:center;margin:0 0 6px;}
  .copy p{margin:0;}
  .copy-slate{color:var(--list);}
  .copy-slate h2{color:#9fdff0;}
  .copy-mist{color:var(--ink);}
  .copy-mist h2{color:var(--ink-dark);}
  .justify{text-align:justify;}
</style>
</head>
<body>

<!-- ===== Outside spread ===== -->
<div class="block panel-slate" style="left:48px;top:240px;width:236px;height:350px;"></div>
<div class="block panel-mist" style="left:284px;top:40px;width:468px;height:550px;"></div>
<div class="photo ph-stones" role="img" aria-label="Stepping stones crossing calm water" style="left:48px;top:40px;width:236px;height:205px;"></div>
<div class="photo ph-falls" role="img" aria-label="Cascading stream flowing over mossy rocks" style="left:517px;top:100px;width:235px;height:395px;"></div>
<div class="photo ph-portrait" role="img" aria-label="Portrait of the hypnotherapist by the sea" style="left:284px;top:415px;width:233px;height:175px;"></div>

<!-- ===== Inside spread ===== -->
<div class="block panel-slate" style="left:52px;top:680px;width:245px;height:440px;"></div>
<div class="block panel-mist-dark" style="left:297px;top:622px;width:455px;height:500px;"></div>
<div class="photo ph-stones-row" role="img" aria-label="Row of stones on still water" style="left:52px;top:622px;width:245px;height:70px;"></div>
<div class="photo ph-hill" role="img" aria-label="Hikers climbing a grassy hill under a cloudy sky" style="left:520px;top:622px;width:232px;height:110px;"></div>

<svg class="waves" viewBox="0 0 800 1200" aria-hidden="true">
  <!-- outside left -->
  <path d="M48 212 C120 188 190 240 284 206 L284 250 L48 250Z" fill="var(--sky)"/>
  <path d="M48 226 C120 204 190 254 284 222 L284 262 L48 262Z" fill="var(--ocean)"/>
  <path d="M48 236 C120 216 190 262 284 232 L284 270 L48 270Z" fill="var(--slate)"/>
  <!-- outside right top curve -->
  <path d="M517 40 L752 40 L752 112 C680 160 600 92 517 118 Z" fill="var(--mist)"/>
  <!-- outside sweeping wave -->
  <path d="M284 395 C380 352 450 385 517 428 C600 478 680 492 752 420 L752 452 C680 520 600 505 517 462 C450 425 380 398 284 425 Z" fill="var(--sky)"/>
  <path d="M284 414 C380 380 450 410 517 455 C600 500 680 512 752 446 L752 470 C680 530 600 522 517 478 C450 440 380 418 284 440 Z" fill="var(--slate)"/>
  <path d="M284 428 C380 398 450 425 517 470 C600 512 680 522 752 462 L752 474 C680 534 600 530 517 484 C450 448 380 428 284 448 Z" fill="var(--seafoam)"/>
  <path d="M517 482 C600 528 680 534 752 476 L752 510 L517 510 Z" fill="var(--mist)"/>
  <!-- inside left -->
  <path d="M52 686 C120 668 200 696 297 674 L297 704 L52 704Z" fill="var(--sky)"/>
  <path d="M52 694 C120 678 200 704 297 684 L297 712 L52 712Z" fill="var(--slate)"/>
  <!-- inside middle/right arc -->
  <path d="M297 706 C360 680 430 662 520 690 C600 714 680 722 752 704 L752 736 L520 736 C430 690 360 700 297 724 Z" fill="var(--slate)"/>
  <path d="M520 732 C600 752 690 748 752 722 L752 770 L520 770Z" fill="var(--mist-dark)"/>
  <path d="M297 722 C360 700 430 692 520 712 C600 736 690 744 752 724 L752 772 L297 772Z" fill="var(--mist-dark)"/>
  <!-- inside bottom bands -->
  <path d="M52 1106 C250 1080 450 1120 752 1092 L752 1172 L52 1172Z" fill="var(--sky)"/>
  <path d="M52 1122 C250 1102 480 1138 752 1112 L752 1172 L52 1172Z" fill="var(--ocean)"/>
  <path d="M52 1138 C260 1122 480 1158 752 1132 L752 1172 L52 1172Z" fill="var(--slate)"/>
  <path d="M52 1154 C260 1144 480 1170 752 1152 L752 1172 L52 1172Z" fill="var(--seafoam)"/>
</svg>

<!-- Outside text -->
<div class="brand" style="left:284px;top:112px;width:233px;">
  <span class="brand-name" style="font-size:15px;">Tidewater</span>
  <span class="brand-sub" style="font-size:9px;">Hypnosis Center</span>
</div>
<div class="brand" style="left:517px;top:98px;width:235px;">
  <span class="brand-name" style="font-size:20px;">Tidewater</span>
  <span class="brand-sub" style="font-size:12px;">Hypnosis Center</span>
</div>

<div class="services">
  <h3>Hypnosis can help you with thefollowing and more:</h3>
  <div class="services-cols">
    <ul>
      <li>Stop Smoking</li><li>Anxiety</li><li>Remove Fears</li><li>Remove Habits</li><li>Drug Abuse</li><li>Motivation</li><li>Public Speaking</li><li>Anger Issues</li><li>Abuse Issues</li><li>Concentration</li><li>Test Anxiety</li><li>Procrastination</li><li>Improve Sports</li>
    </ul>
    <ul>
      <li>Weight Loss</li><li>Stress</li><li>Relationships</li><li>Alcohol Abuse</li><li>Childbirth</li><li>Stage Fright</li><li>Pain Management</li><li>Sexual Issues</li><li>Self-Esteem</li><li>Self-Confidence</li><li>Shyness</li><li>Improve Mood</li><li>Children's Issues</li>
    </ul>
  </div>
  <p class="more">And, More...</p>
  <p class="contact">Contact our office for more information.<br>Your hypnotherapist will be happy to tell you about appointment availability and fees for services.</p>
</div>

<div class="contact-block">
  <p>(360) 555-0142</p>
  <p>TidewaterHypnosisCenter.com</p>
  <p>Copyright © 2014 Tidewater Hypnosis Center.</p>
  <p>All rights reserved.</p>
  <p class="web">TidewaterHypnosisCenter.com</p>
</div>

<p class="tagline">Learn how hypnosis<br>and hypnotherapy can<br>help you succeed.</p>

<!-- Inside text -->
<div class="brand" style="left:297px;top:640px;width:223px;">
  <span class="brand-name" style="font-size:12px;">Tidewater</span>
  <span class="brand-sub" style="font-size:7.5px;">Hypnosis Center</span>
</div>

<div class="copy copy-slate" style="left:62px;top:716px;width:226px;">
  <h2>What is hypnosis?</h2>
  <p>Hypnosis is a state of focused consciousness. Your hypnotherapist will assist you in learning how to achieve this state by guiding you into it.</p>
  <p>Once this has been achieved, you will then receive what are called hypnotic suggestions. These suggestions will enable you to use the power of hypnosis in your life and make the changes you desire.</p>
  <p>Hypnosis is a tool that can help you just, like it has helped millions of other people to take back control of their lives.</p>
  <p>Hypnosis can help you change old habits and to provide you with motivation to do the things that you may have been putting off.</p>
  <p>Hypnosis has been sanctioned and used by the medical community since 1958 to help patients overcome chronic pain, create anesthesia, andheal psychogenic illnesses.</p>
  <p class="justify">Hypnosis and self-hypnosis have been shown to be effective in reducing stress and stress-related illnesses.</p>
  <p>Hypnosis has also been shown to help mothers give birth to their children with little or no pain.</p>
  <p>Is hypnosis safe?</p>
  <p>Hypnosis is safe. It is very similar to experiencing a daydream. Usually you will feel relaxed when doing hypnosis. Hypnosis in and of itself is a very pleasant experience. It is a time to let go of the other thoughts of the day and focus on the issues you came in to work on.</p>
  <p>Scientist, medical professionals, psychologists and hypnotherapists have been using hypnosis for over 200 years and no one has ever been hurt by simply going into hypnosis.</p>
  <h2 style="margin-top:6px;">What is hypnotherapy?</h2>
  <p>Hypnotherapy is the applied use of hypnosis.</p>
  <p>Therapy can be defined as anything that is done to move someone toward health and wholeness.</p>
  <p>Thus, hypnotherapy is the use of hypnosis to help you move toward health and wholeness.</p>
  <p>Hypnotherapy is also used to help you reach goals when nothing else has helped. See the back panel of this brochure to see a list of uses for hypnotherapy.</p>
  <p>Self-hypnosis may also be part of a good hypnotherapy program. Ask your hypnotherapist if using self-hypnosis is recommended to help you reach your goals.</p>
</div>

<div class="copy copy-mist" style="left:307px;top:716px;width:205px;">
  <h2>Can I be hypnotized?</h2>
  <p>Of course you can! You already have been.</p>
  <p>It's easy to go into hypnosis and it is a normal state of mind that everyone has already experienced.</p>
  <p class="justify">In fact, hypnosis is such a normal state of mind, most people usually don't even realize that they are hypnotized. Normal, everyday hypnosis occurs when you are driving down the road and lose track of time, or, when you are focusing on a book or television program and you don't even notice something that is going on around you.</p>
  <p class="justify">When you come in for hypnosis, all you need to do is to be able to follow the instructions of the hypnotherapist and you can put the power of hypnosis to work for you.</p>
  <p>Anyone of with the willingness and ability to follow instructions can experience hypnosis and use it to improve his or her life.</p>
  <p>This includes children and teenagers.</p>
  <h2 style="margin-top:12px;">Who will hypnotize me?</h2>
  <p>Your hypnotist or hypnotherapist is a highly qualified professional. He or she is certified and registered with the Regional Guild of Hypnotists.</p>
  <p class="justify">Your hypnotherapist is bound by professional ethics and the laws of the state in which it is practiced.</p>
  <p>In addition, your hypnotherapist has achieved extra certification in the advanced hypnotherapy system called Core-Path. Rest assured that he or she will treat you with respect, and that your visits are completely confidential.</p>
  <p class="justify">We suggest that you call and speak to us directly so that you can learn more about hypnosis and hypnotherapy. This will allow you to become more familiar with the programs offered and allow us to answer.</p>
</div>

<div class="copy copy-mist" style="left:530px;top:780px;width:214px;">
  <h2>Hypnosis can help you succeed</h2>
  <p style="margin-top:8px;">when nothing else has worked!</p>
  <p>Hypnosis is one of the fastest growing fields of human achievement. As hypnotherapists we are working with people who are frustrated because nothing else has helped them achieve their goals.</p>
  <p>They have tried every other avenue that they can think of without success. We use hypnosis, hypnotherapy and teach self-hypnosis so that people like you can succeed in making important changes.</p>
  <p>Did you know that many of the most successful professional and Olympic teams use hypnosis to help their athletes win? That's true.</p>
  <p>Now you can use this advantage for yourself, whether you are trying to overcome an old problem or if you want to grow to a new level of personal achievement.</p>
  <p>Hypnotherapy can also be used as a complementary treatment for some medical and psychological issues. We can contact your doctor to make sure that using hypnosis is appropriate for your situation.</p>
  <p>Appropriate issues may include pain management, stress related illness and any issue that has been labeled psychogenic in origin.</p>
  <h2 style="margin-top:12px;">Hypnosis can be your tool for success!</h2>
  <p style="margin-top:8px;">We encourage you to call or come into our office and ask us questions about hypnosis and our services. We enjoy answering questions. It is part of our job</p>
</div>

</body>
</html>
```